Ferncrest Dental, LLC business card project

Business card to be designed with current logo.
Dental office- please keep design of card that looks clean and professional.
Please include the following info:
Ferncrest Dental, LLC
Dr. Lorna Pettigrew
2871 Marlowe Street
Bethlehem, PA 18093
610-555-0193
ferncrestdental.office@examplemail.test
Hello everyone-
Reason: Just got back from overseas- will look at all designs and provide feedback. Thank you!
Reason: Polling my friends for the final selection-
thank you to all those that participated- so many talented designers!

```html
<!DOCTYPE html>
<html lang="en">
<head>
<meta charset="utf-8">
<title>Ferncrest Dental, LLC – Business Card</title>
<link href="https://fonts.googleapis.com/css2?family=Questrial&display=swap" rel="stylesheet">
<style>
  :root {
    --lime: #a9cf3a;
    --forest: #5e9c3f;
    --ink: #4a4a4a;
    --ink-soft: #5a5a5a;
    --paper: #ffffff;
    --seam: #ececec;
  }
  * { margin: 0; padding: 0; box-sizing: border-box; }
  html, body {
    width: 1200px; height: 963px; overflow: hidden;
    background: var(--paper);
    font-family: "Questrial", "Century Gothic", sans-serif;
  }
  .sheet { position: relative; width: 1200px; height: 963px; }

  .card { position: absolute; top: 0; height: 963px; width: 600px; background: var(--paper); overflow: hidden; }
  .card--front { left: 0; }
  .card--back { left: 600px; border-left: 1px solid var(--seam); }

  /* front */
  .brand-name {
    position: absolute; left: 0; width: 600px; top: 378px;
    text-align: center; font-size: 46px; color: var(--lime); white-space: nowrap;
  }
  .accent-bar { position: absolute; left: 0; top: 566px; width: 17px; height: 341px; background: var(--lime); }
  .accent-bar::before { content: ""; position: absolute; left: 0; top: 0; width: 6px; height: 100%; background: var(--forest); }

  .holder-name { position: absolute; left: 58px; top: 588px; font-size: 54px; color: var(--ink); white-space: nowrap; }

  .contact { position: absolute; left: 60px; display: flex; align-items: flex-start; gap: 12px; color: var(--ink-soft); font-size: 26px; line-height: 38px; white-space: nowrap; }
  .contact svg { flex: none; fill: var(--ink); }
  .contact--phone { top: 686px; }
  .contact--phone svg { margin-top: 2px; }
  .contact--address { top: 746px; }
  .contact--address svg { margin-top: 8px; }
  .contact--email { top: 842px; font-size: 24px; }
  .contact--email svg { margin-top: 4px; }

  /* back */
  .band { position: absolute; }
  .band--top-dark { left: 72px; top: 0; width: 266px; height: 46px; background: var(--forest); }
  .band--top-lime { left: 334px; top: 0; width: 266px; height: 92px; background: var(--lime); }
  .band--bottom-lime { left: 72px; top: 877px; width: 266px; height: 86px; background: var(--lime); }
  .band--bottom-dark { left: 334px; top: 923px; width: 266px; height: 40px; background: var(--forest); }

  .brand-name--vertical {
    position: absolute; left: 323px; top: 484px;
    transform: translate(-50%, -50%) rotate(90deg);
    font-size: 54px; color: var(--lime); white-space: nowrap;
  }
</style>
</head>
<body>
<main class="sheet">
  <section class="card card--front" aria-label="Card front">
    <p class="brand-name">Ferncrest Dental, LLC</p>
    <div class="accent-bar"></div>
    <h1 class="holder-name">Dr. Lorna Pettigrew</h1>

    <div class="contact contact--phone">
      <svg width="46" height="34" viewBox="0 0 46 34" aria-hidden="true">
        <path d="M4 8 Q23 -2 42 8 L40 14 L32 12 L31 8 Q23 5 15 8 L14 12 L6 14 Z"/>
        <path d="M12 14 L34 14 L40 30 Q40 33 37 33 L9 33 Q6 33 6 30 Z"/>
      </svg>
      <span>610-555-0193</span>
    </div>

    <div class="contact contact--address">
      <svg width="46" height="40" viewBox="0 0 46 40" aria-hidden="true">
        <path d="M23 2 L44 21 L38 21 L38 39 L27 39 L27 28 L19 28 L19 39 L8 39 L8 21 L2 21 Z"/>
      </svg>
      <span>2871 Marlowe Street<br>Bethlehem, PA 18093</span>
    </div>

    <div class="contact contact--email">
      <svg width="48" height="34" viewBox="0 0 48 34" aria-hidden="true">
        <path d="M1 1 H47 V33 H1 Z M5 5 V29 H43 V5 L24 20 Z M8 4 L24 16 L40 4 Z" fill-rule="evenodd"/>
      </svg>
      <span>ferncrestdental.office@examplemail.test</span>
    </div>
  </section>

  <section class="card card--back" aria-label="Card back">
    <div class="band band--top-dark"></div>
    <div class="band band--top-lime"></div>
    <p class="brand-name--vertical">Ferncrest Dental, LLC</p>
    <div class="band band--bottom-lime"></div>
    <div class="band band--bottom-dark"></div>
  </section>
</main>
</body>
</html>
```